Business Cards for a small business advisory (business services)

Professional look. Same as would apply for a lawyer, accountant, or other financial services professional. Please use the logo colors

Target Market(s)

small business owners

Industry/Entity Type

Financial Servics

Contact Information for Business Card

Name: Gavin L. Whitmore, CAIA / Title: Business Advisor / Office #: (718) 294-7716 / Mobile #: (917) 382-5047 / Email: g.whitmore@clearfieldventurepartners.example / Web: www.clearfieldventurepartners.example

Font styles to use
Sans Serif

```html
<!DOCTYPE html>
<html lang="en">
<head>
<meta charset="utf-8">
<title>Clearfield Venture Partners — Business Cards</title>
<link href="https://fonts.googleapis.com/css2?family=Montserrat:wght@400;500;700&display=swap" rel="stylesheet">
<style>
  :root {
    --navy: #1b3564;
    --green: #6fae36;
    --ink: #1c1c1c;
    --paper: #ffffff;
    --backdrop: #e4e2e3;
  }
  * { margin: 0; padding: 0; box-sizing: border-box; }
  html, body { width: 1200px; height: 1108px; overflow: hidden; }
  body {
    background: var(--backdrop);
    font-family: "Montserrat", sans-serif;
    position: relative;
  }
  .card {
    position: absolute;
    width: 740px;
    height: 444px;
    background: var(--paper);
    overflow: hidden;
  }
  .card--front { left: 241px; top: 68px; }
  .card--back { left: 248px; top: 589px; }
  .card__band {
    position: absolute;
    left: 0; right: 0; bottom: 0;
    height: 23px;
    background: var(--navy);
  }
  .brand {
    position: absolute;
    display: flex;
    align-items: center;
    color: var(--navy);
  }
  .brand__dot {
    flex: none;
    border-radius: 50%;
    background: var(--navy);
  }
  .brand__name {
    font-weight: 700;
    line-height: 1.05;
  }
  .brand--small { left: 40px; top: 196px; gap: 12px; }
  .brand--small .brand__dot { width: 38px; height: 38px; }
  .brand--small .brand__name { font-size: 22px; width: 230px; }
  .brand--large { left: 66px; top: 150px; gap: 24px; }
  .brand--large .brand__dot { width: 96px; height: 96px; }
  .brand--large .brand__name { font-size: 44px; width: 480px; }
  .tagline {
    position: absolute;
    left: 186px; top: 262px;
    width: 480px;
    font-size: 14px;
    font-weight: 500;
    color: var(--green);
    line-height: 1.3;
  }
  .divider {
    position: absolute;
    left: 331px; top: 142px;
    width: 2px; height: 178px;
    background: var(--navy);
  }
  .contact {
    position: absolute;
    left: 345px; top: 138px;
  }
  .contact__name {
    font-size: 24px;
    font-weight: 700;
    color: var(--navy);
    line-height: 1.1;
  }
  .contact__title {
    font-size: 15.5px;
    color: var(--ink);
    margin-top: 4px;
  }
  .contact__list { list-style: none; margin-top: 18px; }
  .contact__item {
    display: flex;
    align-items: center;
    gap: 9px;
    font-size: 15.5px;
    color: var(--ink);
    height: 24px;
    white-space: nowrap;
  }
  .contact__item + .contact__item { margin-top: 7px; }
  .contact__item--web { margin-top: 0 !important; }
  .contact__item--small { font-size: 13.6px; }
  .contact__icon { width: 16px; height: 16px; flex: none; fill: var(--navy); }
</style>
</head>
<body>

  <section class="card card--front" aria-label="Card front">
    <div class="brand brand--small">
      <span class="brand__dot"></span>
      <span class="brand__name">Clearfield Venture Partners</span>
    </div>
    <div class="divider"></div>
    <div class="contact">
      <h1 class="contact__name">Gavin L. Whitmore, CAIA</h1>
      <p class="contact__title">Business Advisor</p>
      <ul class="contact__list">
        <li class="contact__item">
          <svg class="contact__icon" viewBox="0 0 24 24" aria-hidden="true"><path d="M6.6 10.8a15.1 15.1 0 0 0 6.6 6.6l2.2-2.2c.3-.3.7-.4 1-.2 1.1.4 2.3.6 3.6.6.6 0 1 .4 1 1V20c0 .6-.4 1-1 1A17 17 0 0 1 3 4c0-.6.4-1 1-1h3.5c.6 0 1 .4 1 1 0 1.3.2 2.5.6 3.6.1.3 0 .7-.2 1z"/></svg>
          (718) 294-7716
        </li>
        <li class="contact__item">
          <svg class="contact__icon" viewBox="0 0 24 24" aria-hidden="true"><path d="M7 1h10a2 2 0 0 1 2 2v18a2 2 0 0 1-2 2H7a2 2 0 0 1-2-2V3a2 2 0 0 1 2-2zm0 3v14h10V4zm5 15.5a1.2 1.2 0 1 0 0 2.4 1.2 1.2 0 0 0 0-2.4z"/></svg>
          (917) 382-5047
        </li>
        <li class="contact__item contact__item--small">
          <svg class="contact__icon" viewBox="0 0 24 24" aria-hidden="true"><path d="M2 5h20v14H2zm2 2v.5l8 5 8-5V7z"/></svg>
          g.whitmore@clearfieldventurepartners.example
        </li>
        <li class="contact__item contact__item--small contact__item--web">
          <svg class="contact__icon" viewBox="0 0 24 24" aria-hidden="true"><path d="M12 2a10 10 0 1 0 0 20 10 10 0 0 0 0-20zm-1 17.9A8 8 0 0 1 4.1 10L9 15v1a2 2 0 0 0 2 2zm6.9-2.5A2 2 0 0 0 16 16h-1v-3a1 1 0 0 0-1-1H8v-2h2a1 1 0 0 0 1-1V7h2a2 2 0 0 0 2-2v-.4a8 8 0 0 1 2.9 12.8z"/></svg>
          www.clearfieldventurepartners.example
        </li>
      </ul>
    </div>
    <div class="card__band"></div>
  </section>

  <section class="card card--back" aria-label="Card back">
    <div class="brand brand--large">
      <span class="brand__dot"></span>
      <span class="brand__name">Clearfield Venture Partners</span>
    </div>
    <p class="tagline">Steady counsel for owners planning to buy, grow or exit a company</p>
    <div class="card__band"></div>
  </section>

</body>
</html>
```